Harbor Athletic Placement Company needs Letterhead design in 2 versions

We would like to design 2 letterhead templates using our existing templates as inspiration. We would like to insert our new logo to replace the old one on both templates. Template 1 is our general letter head and template 2 is our Football specific letterhead. We would also like to incorporate the accent star into the letterhead that was used on my business card, maybe using it as a background shadow effect or something that adds to the design. The Colors we would like to keep from original templates- Blue, Red, Black Silver.

Template 1 updates=
Replace old TLV Fieldmark logo with the new version provided in center top.
add Varsity Pathways Of Westland to top center above new logo in black font
add Bring Skill? Find Signed! in top right with updated font that compliments design.
remove "serving over 2,000 UVLB & ORTE Member Colleges
remove- serving high school and intercollegiate athletics since 1982

Left column updates on template 1 (bullet point use accent star)
*Over 32 Years Of Success In Assisting High School Athletes With Recruiting!
*More than 50,000 Student-Athlete Success Stories!
*Over 1 Billion Dollars in Athletic Scholarships For Fieldmark Families!
*More Than 32,000 Registered College Coaches And 2,000 Colleges And Universities Nationwide!
*Publisher Of Fieldmark Journal- A Top Recruiting Resource Used By Coaches Across The Country!

Remove Countries listed

Keep
College Recruiting, Player Profiles,Recruiting Videos,Vital UVLB Education,Elite Sports Combines, Articles and Recruiting News, Fieldmark Journal.

at bottom of template 1, please add our address and web site

3817 Holloway Lane, Suite# 409, Harbor Point, WL 48213
www.TLVFieldmark-demo.com

Template 2 updates (Football specific template)=
Keep "Fieldmark 720 Prime Talents" in top left but in smaller font above pictures in left column
Add "The Nation's #1 College Football Recruiting Company" under logo in top center (remove College Football Publication)

Left column updates
use magazine cover photos (Markle,Dunstead) remove other 3, make smaller if room needed.
add 2 photos of Wesley and Bryce to left column with caption above photos "Former TLV Fieldmark Student-Athletes"
add=

at bottom of template 2, please add our address and web site

www.TLVFieldmark-demo.com

```html
<!DOCTYPE html>
<html lang="en">
<head>
<meta charset="utf-8">
<title>TLV Fieldmark Letterheads</title>
<link href="https://fonts.googleapis.com/css2?family=Open+Sans:wght@400;600;700&family=Exo+2:ital,wght@1,800&family=Great+Vibes&display=swap" rel="stylesheet">
<style>
:root{
  --red:#e01f26;
  --black:#1c1c1c;
  --grey:#6b6b6b;
  --silver:#d9d9d9;
  --canvas:#eeeeee;
  --paper:#ffffff;
}
*{margin:0;padding:0;box-sizing:border-box}
html,body{width:1200px;height:795px;overflow:hidden;background:var(--canvas);font-family:"Open Sans",sans-serif}
.letterhead{position:absolute;top:75px;width:477px;height:676px;background:var(--paper);box-shadow:0 2px 8px rgba(0,0,0,.25)}
.general{left:103px}
.football{left:618px}
.org-title{position:absolute;top:22px;left:0;width:100%;padding-left:20px;text-align:center;font-size:10.5px;color:var(--black);letter-spacing:.2px}
.brand{position:absolute;top:50px;left:0;width:100%;padding-left:20px;text-align:center;font-size:25px;font-weight:700;color:var(--red);letter-spacing:.5px}
.brand-tagline{position:absolute;top:86px;left:0;width:100%;padding-left:20px;text-align:center;font-size:8px;color:var(--black)}
.program{position:absolute;top:47px;left:21px;font-family:"Exo 2",sans-serif;font-style:italic;font-weight:800;font-size:11.5px;line-height:12.5px;color:var(--black)}
.program span{display:block;color:var(--red)}
.slogan{position:absolute;top:44px;left:360px;font-family:"Exo 2",sans-serif;font-style:italic;font-weight:800;font-size:17px;line-height:17px;color:var(--black)}
.slogan span{display:block;color:var(--red);font-size:14.5px}
.sidebar{position:absolute;top:126px;left:17px;width:75px;border-right:1px solid var(--red);font-size:7.2px;line-height:8.7px;color:var(--black);padding-right:4px}
.general .sidebar{height:429px}
.football .sidebar{left:21px;width:70px;height:488px}
.facts{list-style:none}
.facts li{margin-bottom:15px}
.football .facts{margin-top:4px}
.football .facts li{margin-bottom:5px}
.facts li::before,.services li::before{content:"";display:inline-block;width:4px;height:4px;border-radius:50%;background:var(--red);margin-right:3px;vertical-align:1px}
.services{list-style:none;margin-top:24px;line-height:10.4px}
.services li{padding-left:7px;text-indent:-7px}
.cover{width:53px;height:69px;margin-bottom:7px}
.cover-a{background:linear-gradient(160deg,#3a4b5c,#8a8f94 60%,#c33 100%)}
.cover-b{background:linear-gradient(160deg,#7a2020,#b23a2e 50%,#3b3b40)}
.caption{color:var(--red);margin:0 0 7px}
.photo{width:61px;height:34px;margin-bottom:5px}
.photo-a{background:linear-gradient(135deg,#c9b6a8,#b7262b 60%,#7a7a7a)}
.photo-b{background:linear-gradient(135deg,#2f5a36,#c9a62a 55%,#1f3d25)}
.letter{position:absolute;top:126px;left:118px;width:350px;color:var(--grey);font-size:8.9px;line-height:12.8px}
.greeting{font-weight:700;color:var(--black);margin-bottom:12px}
.letter p{margin-bottom:13px}
.signature{position:absolute;top:470px;left:118px}
.signature .name{font-family:"Great Vibes",cursive;font-size:25px;color:var(--black);line-height:28px}
.signature .role{font-size:8.9px;font-weight:700;color:var(--grey)}
.address{position:absolute;top:644px;left:0;width:100%;text-align:center;font-size:8.3px;line-height:9.8px;color:var(--black)}
</style>
</head>
<body>

<section class="letterhead general">
  <div class="org-title">VARSITY PATHWAYS OF WESTLAND</div>
  <div class="brand">TLV Fieldmark</div>
  <div class="program">FIELDMARK 720<span>Prime Talents</span></div>
  <div class="slogan">Bring Skill?<span>Find Signed!</span></div>

  <aside class="sidebar">
    <ul class="facts">
      <li>Over 32 Years Of Success In Assisting High School Athletes With Recruiting!</li>
      <li>More than 50,000 Student-Athlete Success Stories!</li>
      <li>Over 1 Billion Dollars in Athletic Scholarships For Fieldmark Families!</li>
      <li>More Than 32,000 Registered College Coaches And 2,000 Colleges And Universities Nationwide!</li>
      <li>Publisher Of Fieldmark Journal- A Top Recruiting Resource Used By Coaches Across The Country!</li>
    </ul>
    <ul class="services">
      <li>College Recruiting</li>
      <li>Player Profiles</li>
      <li>Recruiting Videos</li>
      <li>Vital UVLB Education</li>
      <li>Elite Sports Combines</li>
      <li>Articles and Recruiting News</li>
      <li>Fieldmark Journal</li>
    </ul>
  </aside>

  <article class="letter">
    <div class="greeting">Lorem Ipsum,</div>
    <p>Cras mattis consectetur purus sit amet fermentum. Etiam porta sem malesuada magna euismod. Integer posuere erat a ante venenatis dapibus posuere velit aliquet. Cras dapibus ac facilisis in, egestas eget quam. Aenean eu leo quam. Pellentesque ornare quam venenatis vestibulum.</p>
    <p>Vivamus sagittis lacus vel augue laoreet rutrum faucibus dolor auctor. Donec. Etiam porta sem malesuada magna mollis euismod. Morbi leo risus, porta ac consectetur, lum at eros. Nullam id dolor id nibh ultricies vehicula ut id elit.</p>
    <p>Donec id elit non mi porta gravida at eget metus. Fusce dapibus, tellus ac cursus, tortor mauris condimentum nibh, ut fermentum massa justo sit amet risus. Cras justo, dapibus ac facilisis in, egestas eget quam. Cum sociis natoque penatibus et magnis montes, nascetur ridiculus mus.</p>
    <p>Cum sociis natoque penatibus et magnis dis parturient montes, nascetur ridiculus. blandit tempus porttitor. Aenean lacinia bibendum nulla sed consectetur. Lorem ipsum amet, consectetur adipiscing elit.</p>
    <p>Cras justo odio, dapibus ac facilisis in, egestas eget quam. Morbi leo risus, porta ac ac, vestibulum at eros. Duis mollis, est non commodo luctus, nisi erat porttitor ligula, odio sem nec elit. Integer posuere erat a ante venenatis dapibus posuere velit aliquet. sagittis lacus vel augue laoreet rutrum faucibus dolor auctor.</p>
  </article>

  <div class="signature">
    <div class="name">Your Name</div>
    <div class="role">Company Director</div>
  </div>

  <footer class="address">3817 Holloway Lane, Suite# 409, Harbor Point, WL 48213<br>www.TLVFieldmark-demo.com</footer>
</section>

<section class="letterhead football">
  <div class="org-title">VARSITY PATHWAYS OF WESTLAND</div>
  <div class="brand">TLV Fieldmark</div>
  <div class="brand-tagline">The Nation's #1 College Football Recruiting Company</div>
  <div class="program">FIELDMARK 720<span>Prime Talents</span></div>
  <div class="slogan">Bring Skill?<span>Find Signed!</span></div>

  <aside class="sidebar">
    <div class="cover cover-a" role="img" aria-label="Fieldmark Journal cover featuring Markle"></div>
    <div class="cover cover-b" role="img" aria-label="Fieldmark Journal cover featuring Dunstead"></div>
    <p class="caption">Former TLV Fieldmark Student-Athletes</p>
    <div class="photo photo-a" role="img" aria-label="Photo of former student-athlete Wesley in game uniform"></div>
    <div class="photo photo-b" role="img" aria-label="Photo of former student-athlete Bryce in game uniform"></div>
    <ul class="facts">
      <li>Over 32 Years Of Success In Assisting High School Athletes With Recruiting!</li>
      <li>More than 50,000 Student-Athlete Success Stories!</li>
      <li>Over 1 Billion Dollars in Athletic Scholarships For Fieldmark Families!</li>
      <li>More Than 32,000 Registered College Coaches And 2,000 Colleges And Universities Nationwide!</li>
      <li>Publisher Of Fieldmark Journal- A Top Recruiting Resource Used By Coaches Across The Country!</li>
    </ul>
  </aside>

  <article class="letter">
    <div class="greeting">Lorem Ipsum,</div>
    <p>Cras mattis consectetur purus sit amet fermentum. Etiam porta sem malesuada magna euismod. Integer posuere erat a ante venenatis dapibus posuere velit aliquet. Cras dapibus ac facilisis in, egestas eget quam. Aenean eu leo quam. Pellentesque ornare quam venenatis vestibulum.</p>
    <p>Vivamus sagittis lacus vel augue laoreet rutrum faucibus dolor auctor. Donec. Etiam porta sem malesuada magna mollis euismod. Morbi leo risus, porta ac consectetur, lum at eros. Nullam id dolor id nibh ultricies vehicula ut id elit.</p>
    <p>Donec id elit non mi porta gravida at eget metus. Fusce dapibus, tellus ac cursus, tortor mauris condimentum nibh, ut fermentum massa justo sit amet risus. Cras justo, dapibus ac facilisis in, egestas eget quam. Cum sociis natoque penatibus et magnis montes, nascetur ridiculus mus.</p>
    <p>Cum sociis natoque penatibus et magnis dis parturient montes, nascetur ridiculus. blandit tempus porttitor. Aenean lacinia bibendum nulla sed consectetur. Lorem ipsum amet, consectetur adipiscing elit.</p>
    <p>Cras justo odio, dapibus ac facilisis in, egestas eget quam. Morbi leo risus, porta ac ac, vestibulum at eros. Duis mollis, est non commodo luctus, nisi erat porttitor ligula, odio sem nec elit. Integer posuere erat a ante venenatis dapibus posuere velit aliquet. sagittis lacus vel augue laoreet rutrum faucibus dolor auctor.</p>
  </article>

  <div class="signature">
    <div class="name">Your Name</div>
    <div class="role">Company Director</div>
  </div>

  <footer class="address">3817 Holloway Lane, Suite# 409, Harbor Point, WL 48213<br>www.TLVFieldmark-demo.com</footer>
</section>

</body>
</html>
```